Gymnastics and fitness web design

Plavney Gymnastics and fitness centre is opening a new branch in the United States.
Target Audience:
22 to 40 year old people who are not satisfied with their current body figure, shape and size.
and
Our programs
Vexabolt, Sports performance and personal training
DESIGN STYLE:
We want the site to be trendy, edgy and cool. The colors we prefer are blue, black and silver. Th idea is people should get motivated by seeing our website. We don't like adding many text in the design, images oriented design is what we are after.
Contents should be added-
Slider
who we are?
section for our programs
Why us?
Video showing some tutorials
Articles
contact us form with map, Address, Phone number, timings, and social media buttons.

```html
<!DOCTYPE html>
<html lang="en">
<head>
<meta charset="utf-8">
<title>Plavney Gymnastics &amp; Fitness Centre — Contact</title>
<link href="https://fonts.googleapis.com/css2?family=Exo+2:wght@700;800&family=Montserrat:wght@400;500;600;700&display=swap" rel="stylesheet">
<style>
:root{
  --blue:#0b2bd6;
  --blue-bright:#1f45f0;
  --blue-deep:#0a1fa8;
  --black:#000;
  --ink:#111;
  --bar:#e4e4e4;
  --field:#ececec;
  --muted:#8c8c8c;
  --white:#fff;
  --footer-bar:#1d2c8f;
  --head:"Exo 2",sans-serif;
  --body:"Montserrat",sans-serif;
}
*{margin:0;padding:0;box-sizing:border-box}
html,body{width:1200px;height:1200px;overflow:hidden}
body{position:relative;font-family:var(--body);background:var(--black);color:var(--white)}
.abs{position:absolute}

/* top info bar */
.info-bar{left:0;top:0;width:1200px;height:33px;background:var(--bar);color:#555;font-size:7px;line-height:8px}
.info-bar .item{position:absolute;top:7px}
.info-bar .sep{position:absolute;top:5px;width:1px;height:22px;background:#bbb}
.info-bar b{font-weight:600;color:#444}
.btn-appointment{position:absolute;left:797px;top:3px;width:154px;height:24px;background:var(--blue-bright);border:1px solid #2f50d8;color:var(--white);font-size:9px;font-weight:600;display:flex;align-items:center;justify-content:center;border-radius:2px}

/* navigation */
.site-nav{left:0;top:33px;width:1200px;height:73px;background:var(--black)}
.brand{position:absolute}
.brand .name{font-family:var(--head);font-weight:800;color:var(--blue-bright);letter-spacing:1px;line-height:1}
.brand .tag{font-family:var(--body);font-weight:500;color:var(--white);letter-spacing:1.2px}
.site-nav .brand{left:252px;top:17px}
.site-nav .brand .name{font-size:30px}
.site-nav .brand .tag{font-size:8.5px;margin-top:2px}
.menu{position:absolute;top:24px;font-size:12px;font-weight:600}
.menu span{position:absolute;white-space:nowrap}
.menu .active{border:1px solid var(--blue-bright);padding:6px 11px;top:-7px;border-radius:2px}

/* map */
.map{left:0;top:106px;width:1200px;height:269px;background:linear-gradient(120deg,#ecebe8 0%,#e6e5e2 45%,#efe9d9 60%,#e9e9e9 100%)}

/* contact section */
.contact{left:0;top:375px;width:1200px;height:553px;background:var(--blue)}
.contact .photo{position:absolute;left:520px;top:0;width:680px;height:553px;background:radial-gradient(ellipse at 60% 45%,rgba(60,90,255,.55) 0%,rgba(30,60,230,.35) 35%,rgba(11,43,214,0) 70%)}
.section-title{position:absolute;font-family:var(--head);font-weight:800;font-size:20px;letter-spacing:1.6px}
.rule{position:absolute;width:35px;height:3px;background:var(--white)}
.field{position:absolute;left:297px;width:268px;height:33px;background:var(--field);color:var(--muted);font-size:8.5px;padding:0 17px;display:flex;align-items:center;border-radius:1px}
.field.message{align-items:flex-start;padding-top:13px;height:99px}
.btn-submit{position:absolute;left:296px;top:442px;width:150px;height:33px;background:var(--black);font-size:10px;font-weight:700;display:flex;align-items:center;justify-content:center;letter-spacing:.5px}
.hours{position:absolute;left:660px;top:132px;font-size:10px;font-weight:700;line-height:16px}
.hours .row{display:flex}
.hours .day{width:91px}
.details{position:absolute;left:660px;font-size:10.5px;line-height:16px;font-weight:500}

/* footer */
.footer{left:0;top:928px;width:1200px;height:237px;background:var(--black)}
.footer .brand{left:267px;top:54px}
.footer .brand .name{font-size:29px}
.footer .brand .tag{font-size:8.5px;margin-top:2px}
.footer p{position:absolute;font-size:8.5px;line-height:12.8px;color:#8a8a8a}
.col-title{position:absolute;top:52px;font-family:var(--head);font-weight:700;font-size:13px;letter-spacing:.8px}
.links{position:absolute;top:76px;font-size:8.5px;color:#8a8a8a;line-height:19.2px}
.call{position:absolute;left:791px;top:158px;display:flex;align-items:center;gap:6px}
.call .lbl{font-size:12px;line-height:13px}
.call .num{font-size:10px;color:var(--blue-bright)}
.social{position:absolute;left:791px;top:202px;display:flex;gap:11px}
.social span{width:18px;height:18px;border-radius:50%;background:var(--blue-bright);display:block}
.copyright{left:0;top:1165px;width:1200px;height:35px;background:var(--footer-bar);font-size:7.5px;color:#c8cdf0;padding:13px 0 0 266px}
</style>
</head>
<body>

<header class="abs info-bar">
  <div class="item" style="left:252px"><b>Monday - Friday 13:30 - 17:30</b><br>Saturday and Sunday closed</div>
  <div class="sep" style="left:381px"></div>
  <div class="item" style="left:403px"><b>0555 214 7390</b><br><b>info@plavneygfc.com</b></div>
  <div class="sep" style="left:510px"></div>
  <div class="item" style="left:536px"><b>Lorem ipsum dolor sit amet, consectetur adipiscing<br>elit. Sed semper massa sit amet</b></div>
  <div class="btn-appointment">MAKE AN APPOINTMENT</div>
</header>

<nav class="abs site-nav">
  <div class="brand"><div class="name">PLAVNEY</div><div class="tag">GYMNASTICS &amp; FITNESS CENTRE</div></div>
  <div class="menu">
    <span style="left:618px">Home</span>
    <span style="left:686px">About</span>
    <span style="left:756px">Programs</span>
    <span style="left:845px">Blog</span>
    <span class="active" style="left:896px">Contact</span>
  </div>
</nav>

<div class="abs map" role="img" aria-label="Street map showing the centre's location with a red pin"></div>

<section class="abs contact">
  <div class="photo" role="img" aria-label="Blue-toned photo of an athlete training"></div>

  <h2 class="section-title" style="left:296px;top:77px">TALK TO US</h2>
  <div class="rule" style="left:298px;top:112px"></div>
  <div class="field" style="top:140px">First Name*</div>
  <div class="field" style="top:185px">Last Name*</div>
  <div class="field" style="top:229px">Email Address*</div>
  <div class="field" style="top:274px">Contact Number*</div>
  <div class="field message" style="top:319px">Your Message</div>
  <div class="btn-submit">SUBMIT</div>

  <h2 class="section-title" style="left:657px;top:77px">CONTACT DETAILS</h2>
  <div class="rule" style="left:659px;top:112px"></div>
  <div class="hours">
    <div class="row"><span class="day">MONDAY</span><span>13:30 pM - 17:30 PM</span></div>
    <div class="row"><span class="day">TUESDAY</span><span>13:30 AM - 17:30 PM</span></div>
    <div class="row"><span class="day">WEDNESDAY</span><span>Theater from 13h00</span></div>
    <div class="row"><span class="day">THURSDAY</span><span>13h30 AM - 17h30 PM</span></div>
    <div class="row"><span class="day">FRIDAY</span><span>13h30 AM - 17:30 PM</span></div>
    <div class="row"><span class="day">SATURDAY</span><span>09h00-13h00</span></div>
    <div class="row"><span class="day">SUNDAY</span><span>Closed</span></div>
  </div>
  <div class="details" style="top:258px">012 346 7781<br>info@plavneygfc.com</div>
  <div class="details" style="top:306px">Lorem ipsum dolor sit amet, consectetur<br>adipiscing elit. Sed semper</div>
</section>

<footer class="abs footer">
  <div class="brand"><div class="name">PLAVNEY</div><div class="tag">GYMNASTICS &amp; FITNESS CENTRE</div></div>
  <p style="left:266px;top:110px;width:170px">Lorem ipsum dolor sit amet, consectetur adipiscing elit, sed do eiusmod tempor incididunt ut labore et dolore magna aliqua. Ut enim ad minim veniam, quis nostrud exercitation ullamco laboris nisi ut</p>

  <h3 class="col-title" style="left:495px">SITEMAP</h3>
  <div class="links" style="left:495px">Home<br>About<br>Programs<br>Blog<br>Contact</div>

  <h3 class="col-title" style="left:651px">PROGRAMS</h3>
  <div class="links" style="left:652px">Program one<br>Program two<br>Program three<br>program four</div>

  <h3 class="col-title" style="left:792px">IN CASE OF EMERGENCY</h3>
  <p style="left:792px;top:77px;width:155px">Lorem ipsum dolor sit amet, consectetur adipiscing elit, sed do eiusmod tempor incididunt ut labore et dolore magna aliqua. Ut enim ad minim veniam, quis</p>

  <div class="call">
    <svg width="24" height="24" viewBox="0 0 24 24" aria-hidden="true">
      <circle cx="12" cy="12" r="11" fill="none" stroke="#fff" stroke-width="1.5"/>
      <path d="M8.2 6.5l2 2.4-1.2 1.5c.8 1.8 2.2 3.2 4 4l1.5-1.2 2.4 2-1.3 1.8c-4.5-.6-8.2-4.3-8.8-8.8z" fill="none" stroke="#fff" stroke-width="1.3" stroke-linejoin="round"/>
    </svg>
    <div><div class="lbl">Call Us</div><div class="num">+1 (0)00 555 0142</div></div>
  </div>
  <div class="social" aria-label="Social media links"><span></span><span></span><span></span></div>
</footer>

<div class="abs copyright">© 2017 Plavney. All rights reserved</div>

</body>
</html>
```